We need logo design and homepage fora new company based in Estonia called "Tracklane Supply Estonia". We sell railway parts.

Page should look a little like www.brovenhalt-kierner.example

Target market is Estonia and railway builders in Baltic States.

Preferred colour combination may be brown/white.

We need more pages: Company profile/ Productcs / About US

Maybe you can add random railway pictures.

Texts and other pictures we will add later, we dont have any of them right now.

Tracklane Supply Estonia

3 page

Sans Serif

Designer to choose colors to be used in the design.

• Must have a proper and elegant start page

```html
<!DOCTYPE html>
<html lang="en">
<head>
<meta charset="utf-8">
<title>Tracklane Supply Estonia</title>
<link href="https://fonts.googleapis.com/css2?family=Montserrat:wght@400;600;700&family=Open+Sans:wght@400;600&display=swap" rel="stylesheet">
<style>
:root{
  --brown:#6e2f12;
  --brown-dark:#4d1f0a;
  --accent:#8b3d16;
  --ink:#2b2b2b;
  --muted:#7a7a7a;
  --line:#e4e0dc;
  --paper:#ffffff;
  --soft:#f6f4f2;
  --footer:#f1efec;
}
*{margin:0;padding:0;box-sizing:border-box}
html,body{width:1200px;height:3064px;overflow:hidden}
body{font-family:"Open Sans",Arial,sans-serif;color:var(--ink);background:var(--paper);position:relative}
h1,h2,h3,.nav a,.brand,.btn{font-family:"Montserrat",Arial,sans-serif}

/* hero */
.hero{position:absolute;top:0;left:0;width:1200px;height:512px;background:linear-gradient(180deg,#6d6a66 0%,#8a7560 45%,#5a3d2a 100%)}
.hero-photo{position:absolute;inset:0;background:linear-gradient(160deg,#9aa0a4 0%,#7d6a58 40%,#6b4a34 70%,#3f2a1d 100%);opacity:.9}
.hero-shade{position:absolute;inset:0;background:rgba(0,0,0,.28)}
.topbar{position:absolute;top:0;left:0;width:1200px;height:76px;display:flex;align-items:center;justify-content:space-between;padding:0 128px 0 130px}
.brand{color:#fff;font-weight:700;font-size:22px;letter-spacing:.5px}
.nav{display:flex;gap:6px}
.nav a{color:#fff;text-decoration:none;font-size:12px;font-weight:600;padding:10px 14px;letter-spacing:.5px}
.nav a.active{background:var(--paper);color:var(--ink)}
.hero-copy{position:absolute;top:200px;left:0;width:1200px;text-align:center;color:#fff}
.hero-copy h1{font-size:44px;font-weight:700;letter-spacing:1px}
.hero-copy p{font-size:14px;width:560px;margin:14px auto 0;line-height:1.6}

/* welcome */
.welcome{position:absolute;top:512px;left:0;width:1200px;height:248px;background:var(--brown);color:#fff;text-align:center;padding-top:44px}
.welcome h2{font-size:20px;font-weight:700;letter-spacing:.5px}
.welcome .rule{width:60px;height:2px;background:#fff;margin:12px auto 18px}
.welcome p{width:800px;margin:0 auto;font-size:13px;line-height:1.7;opacity:.9}
.btn{display:inline-block;margin-top:22px;border:2px solid #fff;border-radius:20px;padding:8px 22px;font-size:11px;font-weight:600;color:#fff;letter-spacing:.5px}

/* products */
.products{position:absolute;top:760px;left:0;width:1200px;height:1260px;background:var(--paper)}
.section-title{text-align:center;font-size:30px;font-weight:700;color:var(--ink)}
.products .section-title{margin-top:54px}
.section-title+.rule{width:60px;height:3px;background:var(--accent);margin:10px auto 0}
.grid{position:absolute;top:128px;left:136px;width:928px;display:grid;grid-template-columns:repeat(3,296px);column-gap:20px;row-gap:64px}
.card{height:324px;background:var(--paper);box-shadow:0 2px 10px rgba(0,0,0,.12);text-align:center}
.card-photo{height:192px}
.card h3{font-size:12px;font-weight:700;margin-top:20px;letter-spacing:.5px}
.card p{font-size:11px;color:var(--muted);line-height:1.6;width:240px;margin:10px auto 0}
.card .more{display:inline-flex;align-items:center;gap:6px;margin-top:14px;font-family:"Montserrat",Arial,sans-serif;font-size:10px;font-weight:700;color:var(--accent)}
.ph1{background:linear-gradient(135deg,#3f6b96,#d9a441)}
.ph2{background:linear-gradient(135deg,#8e8e8e,#4b4b4b)}
.ph3{background:linear-gradient(135deg,#b7a790,#5b5348)}
.ph4{background:linear-gradient(135deg,#b4b6b8,#56595c)}
.ph5{background:linear-gradient(135deg,#6f6f6f,#2e2e2e)}
.ph6{background:linear-gradient(135deg,#d27a2d,#3d5d7a)}
.ph7{background:linear-gradient(135deg,#7a4a35,#3a2419)}
.ph8{background:linear-gradient(135deg,#5c6066,#1e1f22)}
.ph9{background:linear-gradient(135deg,#8c8c8c,#2a2a2a)}

/* features */
.features{position:absolute;top:2020px;left:0;width:1200px;height:468px;background:var(--paper);border-top:1px solid var(--line)}
.features .section-title{margin-top:74px;font-size:24px}
.features .intro{width:720px;margin:16px auto 0;text-align:center;font-size:11px;color:var(--muted);line-height:1.6}
.feature-row{position:absolute;top:196px;left:220px;width:760px;display:flex;justify-content:space-between}
.feature{width:200px;text-align:center}
.feature svg{display:block;margin:0 auto}
.feature h3{font-size:12px;font-weight:700;margin-top:16px}
.feature p{font-size:11px;color:var(--muted);line-height:1.6;margin-top:8px}

/* map */
.map{position:absolute;top:2488px;left:0;width:1200px;height:272px;background:linear-gradient(135deg,#e6e3dc,#d8d4cc)}
.map-card{position:absolute;top:88px;left:820px;width:240px;background:var(--paper);box-shadow:0 2px 8px rgba(0,0,0,.2);padding:12px 14px;font-size:10px;color:var(--muted);line-height:1.5}
.map-card strong{display:block;color:var(--ink);font-family:"Montserrat",Arial,sans-serif;font-size:11px;margin-bottom:2px}
.pin{position:absolute;top:94px;left:726px}

/* footer */
.footer{position:absolute;top:2760px;left:0;width:1200px;height:304px;background:var(--footer)}
.footer-cols{position:absolute;top:36px;left:130px;width:940px;display:grid;grid-template-columns:180px 300px 270px 190px}
.footer h3{font-size:13px;font-weight:700;margin-bottom:14px}
.footer li{list-style:none;font-size:11px;color:var(--muted);line-height:2}
.footer .news p{font-size:11px;color:var(--muted);line-height:1.6;width:240px}
.field{width:240px;height:30px;border:1px solid var(--line);background:var(--paper);margin-top:12px}
.sub{display:inline-block;margin-top:12px;border:2px solid var(--accent);border-radius:16px;padding:5px 18px;font-family:"Montserrat",Arial,sans-serif;font-size:10px;font-weight:700;color:var(--accent)}
.contact li{display:flex;align-items:center;gap:8px}
.social li{display:flex;align-items:center;gap:10px;line-height:2.7}
.social .dot{width:22px;height:22px;border:1px solid #999;border-radius:50%}
.copyright{position:absolute;bottom:0;left:0;width:1200px;height:44px;border-top:1px solid var(--line);text-align:center;font-size:10px;color:var(--muted);line-height:44px}
</style>
</head>
<body>

<header class="hero">
  <div class="hero-photo" role="img" aria-label="Photo of railway track construction with workers and machinery"></div>
  <div class="hero-shade"></div>
  <div class="topbar">
    <div class="brand">TRACKLANE SUPPLY ESTONIA</div>
    <nav class="nav">
      <a class="active" href="#">HOME</a><a href="#">PROFILE</a><a href="#">PRODUCTS</a><a href="#">ABOUT US</a><a href="#">CONTACT US</a>
    </nav>
  </div>
  <div class="hero-copy">
    <h1>WE SELL RAILWAY PARTS</h1>
    <p>Quality rails, switches, fasteners and track tools delivered across Estonia and the Baltic states for every build.</p>
  </div>
</header>

<section class="welcome">
  <h2>WELCOME TO TRACKLANE SUPPLY ESTONIA</h2>
  <div class="rule"></div>
  <p>We supply railway builders across Estonia, Latvia and Lithuania with dependable track parts. From sleepers and rail clips to switch components and maintenance tools, our stock is chosen for heavy traffic and hard northern winters. Our team helps contractors plan orders, meet deadlines and keep every line running safely for years to come.</p>
  <span class="btn">LEARN MORE</span>
</section>

<section class="products">
  <h2 class="section-title">OUR PRODUCTS</h2>
  <div class="rule"></div>
  <div class="grid">
    <article class="card"><div class="card-photo ph1" role="img" aria-label="Photo of track laying machine"></div><h3>NUMQUAM EIUS MODI</h3><p>Durable track components tested for heavy loads and harsh Baltic winters.</p><span class="more">VIEW MORE <svg width="10" height="8"><path d="M0 4h8M5 1l3 3-3 3" stroke="currentColor" fill="none" stroke-width="1.5"/></svg></span></article>
    <article class="card"><div class="card-photo ph2" role="img" aria-label="Photo of rail wheel parts"></div><h3>NUMQUAM EIUS MODI</h3><p>Durable track components tested for heavy loads and harsh Baltic winters.</p><span class="more">VIEW MORE <svg width="10" height="8"><path d="M0 4h8M5 1l3 3-3 3" stroke="currentColor" fill="none" stroke-width="1.5"/></svg></span></article>
    <article class="card"><div class="card-photo ph3" role="img" aria-label="Photo of railway tracks on gravel"></div><h3>NUMQUAM EIUS MODI</h3><p>Durable track components tested for heavy loads and harsh Baltic winters.</p><span class="more">VIEW MORE <svg width="10" height="8"><path d="M0 4h8M5 1l3 3-3 3" stroke="currentColor" fill="none" stroke-width="1.5"/></svg></span></article>
    <article class="card"><div class="card-photo ph4" role="img" aria-label="Photo of rail fastening system"></div><h3>NUMQUAM EIUS MODI</h3><p>Durable track components tested for heavy loads and harsh Baltic winters.</p><span class="more">VIEW MORE <svg width="10" height="8"><path d="M0 4h8M5 1l3 3-3 3" stroke="currentColor" fill="none" stroke-width="1.5"/></svg></span></article>
    <article class="card"><div class="card-photo ph5" role="img" aria-label="Photo of train bogie assembly"></div><h3>NUMQUAM EIUS MODI</h3><p>Durable track components tested for heavy loads and harsh Baltic winters.</p><span class="more">VIEW MORE <svg width="10" height="8"><path d="M0 4h8M5 1l3 3-3 3" stroke="currentColor" fill="none" stroke-width="1.5"/></svg></span></article>
    <article class="card"><div class="card-photo ph6" role="img" aria-label="Photo of worker maintaining rail equipment"></div><h3>NUMQUAM EIUS MODI</h3><p>Durable track components tested for heavy loads and harsh Baltic winters.</p><span class="more">VIEW MORE <svg width="10" height="8"><path d="M0 4h8M5 1l3 3-3 3" stroke="currentColor" fill="none" stroke-width="1.5"/></svg></span></article>
    <article class="card"><div class="card-photo ph7" role="img" aria-label="Photo of stacked rail sleepers"></div><h3>NUMQUAM EIUS MODI</h3><p>Durable track components tested for heavy loads and harsh Baltic winters.</p><span class="more">VIEW MORE <svg width="10" height="8"><path d="M0 4h8M5 1l3 3-3 3" stroke="currentColor" fill="none" stroke-width="1.5"/></svg></span></article>
    <article class="card"><div class="card-photo ph8" role="img" aria-label="Photo of locomotive wheel set"></div><h3>NUMQUAM EIUS MODI</h3><p>Durable track components tested for heavy loads and harsh Baltic winters.</p><span class="more">VIEW MORE <svg width="10" height="8"><path d="M0 4h8M5 1l3 3-3 3" stroke="currentColor" fill="none" stroke-width="1.5"/></svg></span></article>
    <article class="card"><div class="card-photo ph9" role="img" aria-label="Photo of steam engine drive wheels"></div><h3>NUMQUAM EIUS MODI</h3><p>Durable track components tested for heavy loads and harsh Baltic winters.</p><span class="more">VIEW MORE <svg width="10" height="8"><path d="M0 4h8M5 1l3 3-3 3" stroke="currentColor" fill="none" stroke-width="1.5"/></svg></span></article>
  </div>
</section>

<section class="features">
  <h2 class="section-title">OUR FEATURES</h2>
  <p class="intro">Fast delivery across the Baltic region, certified parts from trusted mills and a team that knows railway building inside out. We keep stock ready so your project never waits.</p>
  <div class="feature-row">
    <div class="feature">
      <svg width="104" height="104" viewBox="0 0 104 104"><path d="M14 70A42 42 0 1 1 90 70" fill="none" stroke="var(--accent)" stroke-width="6" stroke-linecap="round"/><path d="M38 52l10 10 18-20" fill="none" stroke="var(--accent)" stroke-width="4"/></svg>
      <h3>NUMQUAM EIUS MODI</h3>
      <p>Certified parts checked for quality before every single shipment leaves us.</p>
    </div>
    <div class="feature">
      <svg width="104" height="104" viewBox="0 0 104 104"><path d="M14 70A42 42 0 1 1 90 70" fill="none" stroke="var(--accent)" stroke-width="6" stroke-linecap="round"/><circle cx="52" cy="50" r="12" fill="none" stroke="var(--accent)" stroke-width="4"/><circle cx="52" cy="50" r="4" fill="var(--accent)"/></svg>
      <h3>NUMQUAM EIUS MODI</h3>
      <p>Technical advice from engineers who plan and build railway lines daily.</p>
    </div>
    <div class="feature">
      <svg width="104" height="104" viewBox="0 0 104 104"><path d="M14 70A42 42 0 1 1 90 70" fill="none" stroke="var(--accent)" stroke-width="6" stroke-linecap="round"/><path d="M40 40h16l12 12-12 12-16-16z" fill="none" stroke="var(--accent)" stroke-width="4"/></svg>
      <h3>NUMQUAM EIUS MODI</h3>
      <p>Fair prices and steady stock for contractors across all Baltic states.</p>
    </div>
  </div>
</section>

<section class="map" role="img" aria-label="Street map showing the company location in Tallinn">
  <svg class="pin" width="22" height="30" viewBox="0 0 22 30"><path d="M11 0C5 0 0 5 0 11c0 8 11 19 11 19s11-11 11-19C22 5 17 0 11 0z" fill="#c8372d"/><circle cx="11" cy="11" r="4" fill="#fff"/></svg>
  <div class="map-card"><strong>TRACKLANE SUPPLY ESTONIA</strong>Rööpa tee 12, 10111 Tallinn<br>Estonia, open Mon–Fri</div>
</section>

<footer class="footer">
  <div class="footer-cols">
    <div>
      <h3>QUICK LINKS</h3>
      <ul><li>Home</li><li>Profile</li><li>Products</li><li>About Us</li><li>Contact</li></ul>
    </div>
    <div class="news">
      <h3>NEWSLETTER</h3>
      <p>Enter your email below to receive the latest news and offers from our team.</p>
      <div class="field"></div>
      <span class="sub">SUBSCRIBE</span>
    </div>
    <div class="contact">
      <h3>CONTACT DETAILS</h3>
      <ul>
        <li><svg width="12" height="12" viewBox="0 0 12 12"><path d="M2 1l3 0 1 3-2 1a7 7 0 0 0 3 3l1-2 3 1 0 3C6 11 1 6 2 1z" fill="var(--accent)"/></svg>+372 5550 1234</li>
        <li><svg width="12" height="12" viewBox="0 0 12 12"><path d="M2 1l3 0 1 3-2 1a7 7 0 0 0 3 3l1-2 3 1 0 3C6 11 1 6 2 1z" fill="var(--accent)"/></svg>+372 5550 5678</li>
        <li><svg width="12" height="12" viewBox="0 0 12 12"><rect x="1" y="2.5" width="10" height="7" fill="none" stroke="var(--accent)"/><path d="M1 3l5 4 5-4" fill="none" stroke="var(--accent)"/></svg>hello@tracklane-supply.example</li>
        <li><svg width="12" height="12" viewBox="0 0 12 12"><path d="M6 0C3.5 0 2 2 2 4c0 3 4 8 4 8s4-5 4-8c0-2-1.5-4-4-4z" fill="var(--accent)"/></svg>Rööpa tee 12, Tallinn</li>
      </ul>
    </div>
    <div class="social">
      <h3>FOLLOW US</h3>
      <ul><li><span class="dot"></span>Newsfeed</li><li><span class="dot"></span>Shortposts</li><li><span class="dot"></span>Circles</li><li><span class="dot"></span>Worknet</li></ul>
    </div>
  </div>
  <div class="copyright">© 2017 Tracklane Supply Estonia. All rights reserved.</div>
</footer>

</body>
</html>
```